Web development startup company needs a web design

We need a design for a company starting out, based in Australia. The business focuses on Quarvo database solutions - Quarvo database development, web development, support, etc. As such, needs a professional look and feel to it.
I'm thinking a single page design where the user can either click a nav bar to go to the relevant section in the page or scroll down is the best shot - but I'm no designer so happy with any suggestions.
I envisions three sections to the page
1. An about us:
2. Project listing
3. Contact form.
Industry/Entity Type
Business
Coding
Coded - Design and coding required
Number of Pages Required
1 page
Look and feel

```html
<!DOCTYPE html>
<html lang="en">
<head>
<meta charset="utf-8">
<title>Tidewell Data Solutions</title>
<link href="https://fonts.googleapis.com/css2?family=Lato:wght@300;400;700;900&display=swap" rel="stylesheet">
<style>
:root{
  --blue:#1bb8e6;
  --ink:#333a40;
  --muted:#8a9096;
  --light:#f3f4f5;
  --dark:#2b2d30;
  --darker:#222326;
  --white:#fff;
}
*{box-sizing:border-box;margin:0;padding:0}
html,body{width:1200px;height:2899px;overflow:hidden}
body{font-family:"Lato",sans-serif;color:var(--ink);background:var(--white);position:relative}
section,header,footer{position:absolute;left:0;width:1200px}
.center{text-align:center}
.section-title{font-size:20px;font-weight:400;letter-spacing:.5px;text-transform:uppercase}
.section-title b{font-weight:400;color:var(--blue)}
.rule{width:34px;height:2px;background:var(--blue);margin:10px auto 0}

/* header */
.site-header{top:0;height:58px;background:var(--white);border-bottom:1px solid #e8e8e8}
.brand{position:absolute;left:290px;top:12px;display:flex;align-items:center;gap:8px}
.brand-dot{width:30px;height:30px;border-radius:50%;border:3px solid var(--blue)}
.brand-name{font-size:17px;font-weight:700;color:var(--blue);line-height:1}
.brand-name small{display:block;font-size:8px;letter-spacing:3px;font-weight:400;margin-top:3px}
.nav{position:absolute;left:675px;top:22px;display:flex;gap:34px;font-size:10px;font-weight:700;color:var(--muted);letter-spacing:.5px}
.nav .active{color:var(--blue)}

/* hero */
.hero{top:58px;height:449px;background:linear-gradient(160deg,#5c5e61 0%,#3b3c3f 45%,#1e1f21 100%)}
.hero-title{position:absolute;top:180px;width:100%;text-align:center;color:var(--white);font-size:29px;font-weight:300}
.hero-title b{color:var(--blue);font-weight:400}
.hero-sub{position:absolute;top:222px;width:100%;text-align:center;color:var(--white);font-size:14px;font-weight:700}
.scroll-cue{position:absolute;left:584px;top:380px}

/* about */
.about{top:507px;height:334px;background:var(--white)}
.about-art{position:absolute;left:350px;top:48px;width:230px;height:170px;border-radius:6px;background:radial-gradient(circle at 50% 45%,#d9dde1,#eef0f2 70%)}
.about-text{position:absolute;left:638px;top:62px;width:470px}
.eyebrow{font-size:10px;color:var(--muted);text-transform:uppercase;letter-spacing:1px}
.about-text h2{font-size:20px;font-weight:400;margin:4px 0 6px;text-transform:uppercase}
.about-text .rule{margin:0 0 14px}
.about-text p{font-size:10px;line-height:1.6;color:var(--muted)}
.bullets{list-style:none;margin-top:14px}
.bullets li{font-size:10px;color:var(--muted);line-height:2.3;display:flex;align-items:center;gap:10px}
.bullets li::before{content:"";width:7px;height:7px;background:var(--blue)}

/* facts */
.facts{top:841px;height:240px;background:var(--blue);color:var(--white)}
.facts .section-title{padding-top:42px}
.facts .rule{background:var(--white)}
.fact{position:absolute;top:96px;width:130px;text-align:center}
.fact-num{font-size:46px;font-weight:700;line-height:1}
.fact-label{font-size:11px;font-weight:700;text-transform:uppercase;margin-top:8px}
.fact-text{font-size:9px;line-height:1.5;margin-top:10px}

/* services */
.services{top:1081px;height:340px;background:var(--white)}
.services .section-title{padding-top:50px}
.services-intro{width:540px;margin:22px auto 0;font-size:10px;line-height:1.6;color:var(--muted)}
.service{position:absolute;top:180px;width:140px;text-align:center}
.service-icon{width:58px;height:58px;border-radius:50%;border:2px solid var(--blue);margin:0 auto;display:flex;align-items:center;justify-content:center}
.service h3{font-size:13px;font-weight:400;margin-top:12px;white-space:nowrap}
.service p{font-size:9px;color:var(--muted);line-height:1.5;margin-top:4px}

/* clients */
.clients{top:1421px;height:261px;background:linear-gradient(135deg,#3a3c3f,#1f2022)}
.clients .section-title{padding-top:62px;color:var(--white)}
.client-row{position:absolute;top:138px;left:290px;width:640px;display:flex;justify-content:space-between}
.client-name{font-size:24px;font-weight:700;color:#d8d8d8;letter-spacing:1px}
.dots{position:absolute;left:0;width:100%;display:flex;justify-content:center;gap:6px}
.dots span{width:6px;height:6px;border-radius:50%;background:#888}
.dots span.on{background:var(--blue)}

/* portfolio */
.portfolio{top:1682px;height:528px;background:var(--white)}
.portfolio .section-title{padding-top:56px}
.filters{position:absolute;top:126px;width:100%;text-align:center;font-size:10px;color:var(--muted)}
.filters span{margin:0 7px}
.filters .active{color:var(--blue)}
.grid{position:absolute;top:151px;left:0;width:1200px;display:grid;grid-template-columns:repeat(6,200px);grid-auto-rows:93px}
.tile{display:block}
.load-more{position:absolute;left:555px;top:456px;width:90px;height:32px;border:1px solid #bbb;font-size:9px;font-weight:700;display:flex;align-items:center;justify-content:center}

/* testimonials */
.testimonials{top:2210px;height:270px;background:linear-gradient(160deg,#6a6c6f,#3c3d40 60%,#2c2d30)}
.testimonials .section-title{padding-top:56px;color:var(--white)}
.quote{width:520px;margin:16px auto 0;font-size:9px;line-height:1.6;color:#e4e4e4;text-transform:uppercase}
.author{margin-top:24px;font-size:10px;color:var(--white)}

/* contact */
.contact{top:2480px;height:390px;background:var(--dark)}
.contact .section-title{padding-top:76px;color:var(--white)}
.contact-intro{width:500px;margin:16px auto 0;font-size:9px;line-height:1.6;color:#b9b9b9}
.form{position:absolute;left:400px;top:160px;width:420px}
.field{border:1px solid #4a4c50;background:#2f3134;color:#9a9a9a;font-size:9px;padding:8px 10px;text-transform:uppercase}
.row{display:flex;gap:13px}
.row .field{flex:1;height:28px}
.message{height:86px;margin-top:13px}
.send{position:absolute;left:151px;top:150px;width:121px;height:25px;background:#5a5c60;color:var(--white);font-size:9px;display:flex;align-items:center;justify-content:center;text-transform:uppercase}

/* footer */
.site-footer{top:2870px;height:29px;background:var(--blue);color:var(--white)}
.copyright{position:absolute;left:290px;top:9px;font-size:8px}
.social{position:absolute;left:860px;top:6px;display:flex;gap:8px}
.social span{width:17px;height:17px;border-radius:50%;background:var(--white);opacity:.9}
</style>
</head>
<body>

<header class="site-header">
  <div class="brand"><span class="brand-dot"></span><span class="brand-name">Tidewell Data<small>SOLUTIONS</small></span></div>
  <nav class="nav"><span class="active">HOME</span><span>ABOUT US</span><span>PROJECTS</span><span>CONTACT US</span></nav>
</header>

<section class="hero" role="img" aria-label="Dim office desk with a computer monitor by a window">
  <h1 class="hero-title">Welcome On <b>Tidewell Data Solutions</b></h1>
  <p class="hero-sub">Lorem ipsum dolor sit amet, consectetur adipiscing elit</p>
  <svg class="scroll-cue" width="32" height="32" viewBox="0 0 32 32"><circle cx="16" cy="16" r="14" fill="none" stroke="#fff" stroke-width="1.5"/><line x1="16" y1="10" x2="16" y2="21" stroke="#fff" stroke-width="1.5"/></svg>
</section>

<section class="about" id="about">
  <div class="about-art" role="img" aria-label="Illustration of a central server connected to several laptops"></div>
  <div class="about-text">
    <div class="eyebrow">About us</div>
    <h2>Some words about us</h2>
    <div class="rule"></div>
    <p>Lorem ipsum is simply dummy text of the printing and typesetting industry. Lorem ipsum has been the industry's standard dummy text ever since the 1500s, when an unknown printer took a galley of type and scrambled it to make a type specimen book. It has survived not only five centuries, but also the leap into electronic typesetting, remaining essentially unchanged.</p>
    <ul class="bullets">
      <li>Duis aute irure dolor in reprehenderit in voluptate velit esse cillum dolore</li>
      <li>Duis aute irure dolor in reprehenderit in voluptate velit esse</li>
      <li>Duis aute irure dolor in reprehenderit</li>
      <li>Duis aute irure dolor in reprehenderit in voluptate velit dolore</li>
    </ul>
  </div>
</section>

<section class="facts">
  <h2 class="section-title center">Some fun facts</h2>
  <div class="rule"></div>
  <div class="fact" style="left:294px"><div class="fact-num">120</div><div class="fact-label">Projects</div><p class="fact-text">Lorem ipsum dolor sit amet, consectetur adipiscing elit, sed do eiusmod</p></div>
  <div class="fact" style="left:465px"><div class="fact-num">220</div><div class="fact-label">Clients</div><p class="fact-text">Lorem ipsum dolor sit amet, consectetur adipiscing elit, sed do eiusmod</p></div>
  <div class="fact" style="left:625px"><div class="fact-num">76</div><div class="fact-label">Database Solution</div><p class="fact-text">Lorem ipsum dolor sit amet, consectetur adipiscing elit, sed do eiusmod</p></div>
  <div class="fact" style="left:787px"><div class="fact-num">2K</div><div class="fact-label">Connections</div><p class="fact-text">Lorem ipsum dolor sit amet, consectetur adipiscing elit, sed do eiusmod</p></div>
</section>

<section class="services">
  <h2 class="section-title center">Take a look at our <b>services</b></h2>
  <div class="rule"></div>
  <p class="services-intro center">Lorem ipsum dolor sit amet, consectetur adipiscing elit, sed do eiusmod tempor incididunt ut labore et dolore magna aliqua. Ut enim ad minim veniam, quis nostrud exercitation ullamco laboris nisi ut aliquip ex ea commodo consequat. Duis aute irure dolor in reprehenderit in voluptate velit esse cillum dolore eu fugiat nulla pariatur, excepteur sint occaecat.</p>
  <div class="service" style="left:292px"><div class="service-icon"><svg width="26" height="26" viewBox="0 0 26 26"><rect x="4" y="4" width="18" height="18" rx="3" fill="none" stroke="#333" stroke-width="1.6"/><path d="M10 9l-3 4 3 4M16 9l3 4-3 4" fill="none" stroke="#333" stroke-width="1.6"/></svg></div><h3>Database Development</h3><p>Lorem ipsum dolor sit amet, consectetur adipiscing elit</p></div>
  <div class="service" style="left:452px"><div class="service-icon"><svg width="26" height="26" viewBox="0 0 26 26"><rect x="3" y="5" width="20" height="14" fill="none" stroke="#333" stroke-width="1.6"/><line x1="9" y1="22" x2="17" y2="22" stroke="#333" stroke-width="1.6"/><path d="M11 10l-2 2 2 2M15 10l2 2-2 2" fill="none" stroke="#333" stroke-width="1.4"/></svg></div><h3>WebDevelopment</h3><p>Lorem ipsum dolor sit amet, consectetur adipiscing elit</p></div>
  <div class="service" style="left:614px"><div class="service-icon"><svg width="26" height="26" viewBox="0 0 26 26"><rect x="9" y="3" width="8" height="7" fill="#333"/><rect x="3" y="15" width="8" height="7" fill="#333"/><rect x="15" y="15" width="8" height="7" fill="#333"/></svg></div><h3>Database Supports</h3><p>Lorem ipsum dolor sit amet, consectetur adipiscing elit</p></div>
  <div class="service" style="left:779px"><div class="service-icon"><svg width="26" height="26" viewBox="0 0 26 26"><circle cx="10" cy="12" r="6" fill="none" stroke="#333" stroke-width="2.5" stroke-dasharray="3 2"/><circle cx="18" cy="18" r="4" fill="none" stroke="#333" stroke-width="2" stroke-dasharray="2 2"/></svg></div><h3>Database Solution</h3><p>Lorem ipsum dolor sit amet, consectetur adipiscing elit</p></div>
</section>

<section class="clients" role="img" aria-label="Darkened photo of a laptop on a desk behind the client names">
  <h2 class="section-title center">Some of our <b>clients</b></h2>
  <div class="rule"></div>
  <div class="client-row"><span class="client-name">NORVALE</span><span class="client-name">Brekstad</span><span class="client-name">Solvanta</span><span class="client-name">HARLOW&amp;FINCH</span></div>
  <div class="dots" style="top:202px"><span class="on"></span><span></span><span></span></div>
</section>

<section class="portfolio" id="projects">
  <h2 class="section-title center">Our portfolio</h2>
  <div class="rule"></div>
  <div class="filters"><span class="active">All</span>/<span>Quarvo Development</span>/<span>Web Development</span>/<span>Others</span></div>
  <div class="grid">
    <span class="tile" role="img" aria-label="Photo of notebooks and a phone on a desk" style="background:linear-gradient(135deg,#b7916b,#e9e2d6)"></span>
    <span class="tile" role="img" aria-label="Photo of concert stage lights" style="background:linear-gradient(135deg,#1c2b55,#8fa6d8)"></span>
    <span class="tile" role="img" aria-label="Photo of a laptop on a wooden table" style="background:linear-gradient(135deg,#a6784e,#dcd4c8)"></span>
    <span class="tile" role="img" aria-label="Photo of wind turbines under a sky" style="background:linear-gradient(180deg,#9fb6c9,#e3ebf0)"></span>
    <span class="tile" role="img" aria-label="Photo of notebooks and a phone on a desk" style="background:linear-gradient(135deg,#b7916b,#e9e2d6)"></span>
    <span class="tile" role="img" aria-label="Photo of concert stage lights" style="background:linear-gradient(135deg,#1c2b55,#8fa6d8)"></span>
    <span class="tile" role="img" aria-label="Photo of a city street with buildings" style="background:linear-gradient(135deg,#5a5f66,#c2c6cb)"></span>
    <span class="tile" role="img" aria-label="Photo of a coffee cup and tablet" style="background:linear-gradient(135deg,#6b4c36,#c8b39c)"></span>
    <span class="tile" role="img" aria-label="Photo of a smartphone on a desk" style="background:linear-gradient(135deg,#3c3f44,#9ea3a8)"></span>
    <span class="tile" role="img" aria-label="Photo of an open road at dusk" style="background:linear-gradient(180deg,#7d8fa3,#3c4048)"></span>
    <span class="tile" role="img" aria-label="Photo of a city street with buildings" style="background:linear-gradient(135deg,#5a5f66,#c2c6cb)"></span>
    <span class="tile" role="img" aria-label="Photo of a coffee cup and tablet" style="background:linear-gradient(135deg,#6b4c36,#c8b39c)"></span>
    <span class="tile" role="img" aria-label="Photo of colourful shelves" style="background:linear-gradient(135deg,#a88a3e,#4f3a2a)"></span>
    <span class="tile" role="img" aria-label="Photo of a crowd with raised hands" style="background:linear-gradient(135deg,#1e2230,#b7c0cf)"></span>
    <span class="tile" role="img" aria-label="Photo of desert sand dunes" style="background:linear-gradient(180deg,#e7e1d7,#b8ab97)"></span>
    <span class="tile" role="img" aria-label="Photo of a sunlit field" style="background:linear-gradient(180deg,#d9dde0,#8d8f87)"></span>
    <span class="tile" role="img" aria-label="Photo of colourful shelves" style="background:linear-gradient(135deg,#a88a3e,#4f3a2a)"></span>
    <span class="tile" role="img" aria-label="Photo of a crowd with raised hands" style="background:linear-gradient(135deg,#1e2230,#b7c0cf)"></span>
  </div>
  <div class="load-more">LOAD MORE</div>
</section>

<section class="testimonials" role="img" aria-label="Grey photo of an empty meeting room behind the testimonial">
  <h2 class="section-title center">Our happy clients &amp; there comments</h2>
  <div class="rule"></div>
  <p class="quote center">Lorem ipsum dolor sit amet, consectetur adipiscing elit, sed do eiusmod tempor incididunt ut labore et dolore magna aliqua. Ut enim ad minim veniam, quis nostrud exercitation ullamco laboris nisi ut aliquip ex ea commodo consequat duis aute irure dolor in reprehenderit.</p>
  <p class="author center">Sam Reyes, CEO Company Name</p>
  <div class="dots" style="top:246px"><span class="on"></span><span></span><span></span></div>
</section>

<section class="contact" id="contact">
  <h2 class="section-title center">Feel free to <b>contact us</b></h2>
  <div class="rule"></div>
  <p class="contact-intro center">Lorem ipsum dolor sit amet, consectetur adipiscing elit, sed do eiusmod tempor incididunt ut labore et dolore magna aliqua. Ut enim ad minim veniam, quis nostrud exercitation ullamco laboris nisi ut aliquip ex ea commodo.</p>
  <div class="form">
    <div class="row"><div class="field">Name</div><div class="field">Email</div></div>
    <div class="field message">Message</div>
    <div class="send">Send message</div>
  </div>
</section>

<footer class="site-footer">
  <span class="copyright">Copyright © 2015 Tidewell Data Solutions</span>
  <div class="social"><span></span><span></span><span></span><span></span></div>
</footer>

</body>
</html>
```